Jackpot Display Wallpaper Design

We develop Jackpot Systems for Casinos and have a web based Jackpot Odometer display. Our software works by superimposing dynamic content over a fixed background.

We require the design of a fixed background of dimensions 1920 x 1080 incorporating higher quality graphical design work and creative ideas.

See File 4 below - "High Hand TEMPLATE". The finished work will resemble this image, with the grey background replaced with your creative design. The black panels will be replaced with your panels, with nice borders and interior shading or pattern. Our software will dynamically superimpose content over the panels. The panels should be of similar size and location to those shown although this is not strictly rigid and you can relocate or resize panels to a limited extent.

The end result when our software runs is something like File 5 below - "High Hand SAMPLE RESULT". Note that the example shows a patterned blue background, a red logo area, and grey shading within the panels.

The text within the panels is rendered dynamically by our application.

** This is a very plain design and only intended to illustrate how we superimpose text and playing cards onto a background. Do not take any design cues from this image.

Please provide the background, and blank panels. The panels can (and should) have some texture or shading that will look good when we render text over them.

Feel free to suggest a font and/or text color that you think would look good against your background and we can render the content in the font / color you suggest.

Target Market(s)

Poker Room facilities and Casinos

Industry/Entity Type

Software

Font styles to use
Sans Serif

Requirements
Must have
• - A graphic design based on the template called High Hand TEMPLATE.
• - 1920 x 1080 Photoshop image using separate layers.
• - The design needs to be edgy and reflect gaming, casinos and poker rooms.
Nice to have
• -Please see files 1, 2, and 3 below by way of "edgy" style guide.
• - For files 1, 2, 3 - ignore the "Bad Beat" wording but focus on the design style by way of example.
• - The background may or may not include the words "Poker" and / or "Jackpot"
• - You can fill in the panels with some sample content to illustrate how it will look.
• - The area at bottom containing scrolling text may be a frame with a border or just an area where we superimpose the scrolling text.

```html
<!DOCTYPE html>
<html lang="en">
<head>
<meta charset="utf-8">
<title>Royal Flush Jackpot Display</title>
<link rel="stylesheet" href="https://fonts.googleapis.com/css2?family=Archivo+Black&family=Arimo:wght@700&display=swap">
<style>
  :root {
    --sky-top: #ffc81a;
    --sky-mid: #ff9a10;
    --sky-low: #ff3c0c;
    --panel: #0d0d0d;
    --panel-hi: #3a3a3a;
    --panel-edge: #1c1c1c;
    --rod: #b9b9b9;
    --rod-dark: #6d6d6d;
    --ink: #ffffff;
    --logo-ink: #d6d6d6;
    --card: #fbfbfb;
    --card-red: #e0101e;
    --card-black: #111111;
  }
  * { box-sizing: border-box; margin: 0; padding: 0; }
  html, body { width: 1200px; height: 675px; overflow: hidden; }
  body { font-family: "Archivo Black", "Arial Black", sans-serif; color: var(--ink); }

  .display {
    position: relative; width: 1200px; height: 675px; overflow: hidden;
    background:
      radial-gradient(ellipse 60% 50% at 50% 45%, rgba(255,230,120,.25), transparent 70%),
      linear-gradient(180deg, var(--sky-top) 0%, var(--sky-mid) 50%, var(--sky-low) 100%);
  }
  .frames { position: absolute; inset: 0; }

  .panel-bar {
    position: absolute; left: 379px; width: 442px; height: 40px;
    background: linear-gradient(180deg, var(--panel-hi) 0%, var(--panel) 40%, var(--panel) 80%, var(--panel-edge) 100%);
    border-radius: 4px;
    box-shadow: 0 3px 6px rgba(0,0,0,.35);
    display: flex; align-items: center; justify-content: center;
    font-size: 19px; letter-spacing: .5px;
  }
  .panel-bar--jackpot { top: 156px; }
  .panel-bar--bonus { top: 390px; }
  .panel-bar--winner { top: 586px; font-family: "Arimo", Arial, sans-serif; font-weight: 700; font-size: 20px; letter-spacing: .6px; }

  .brand-name {
    position: absolute; left: 448px; top: 50px; width: 300px; text-align: center;
    font-size: 34px; color: var(--logo-ink); letter-spacing: 1px;
  }

  .odometer-band {
    position: absolute; left: 0; top: 250px; width: 1200px; height: 86px;
    background: linear-gradient(180deg, #2d2d2d 0%, #0a0a0a 35%, #050505 70%, #262626 100%);
  }
  .odometer { position: absolute; top: 220px; left: 0; width: 1200px; height: 146px; }
  .digit {
    position: absolute; top: 0; width: 114px; height: 146px;
    background: linear-gradient(180deg, #444 0%, #111 14%, #050505 50%, #111 86%, #444 100%);
    border-radius: 10px;
    border-left: 2px solid #2a2a2a; border-right: 2px solid #2a2a2a;
    display: flex; align-items: center; justify-content: center;
    font-size: 122px; line-height: 1;
  }
  .separator {
    position: absolute; top: 92px; font-size: 60px; line-height: 1;
  }

  .prize, .countdown { position: absolute; top: 470px; }
  .prize { left: 310px; }
  .countdown { left: 805px; }
  .stat-label { font-size: 16px; letter-spacing: .3px; }
  .countdown .stat-label { font-size: 13px; }
  .stat-value { font-size: 30px; margin-top: 2px; }

  .hand { position: absolute; top: 461px; left: 0; }
  .card {
    position: absolute; top: 0; width: 69px; height: 100px;
    background: var(--card); border-radius: 4px;
    box-shadow: 0 2px 4px rgba(0,0,0,.4);
    font-family: "Arimo", Arial, sans-serif; font-weight: 700;
  }
  .card--red { color: var(--card-red); }
  .card--black { color: var(--card-black); }
  .card-corner { position: absolute; font-size: 10px; line-height: 10px; text-align: center; }
  .card-corner--top { left: 3px; top: 3px; }
  .card-corner--bottom { right: 3px; bottom: 3px; transform: rotate(180deg); }
  .card-pip { position: absolute; inset: 0; display: flex; align-items: center; justify-content: center; font-size: 26px; }

  .news-band {
    position: absolute; left: 0; top: 632px; width: 1200px; height: 43px;
    background: linear-gradient(180deg, #303030 0%, #0b0b0b 35%, #050505 100%);
    display: flex; align-items: center; justify-content: center;
    font-size: 19px; letter-spacing: .5px;
  }
</style>
</head>
<body>
<main class="display">
  <svg class="frames" width="1200" height="675" viewBox="0 0 1200 675" aria-hidden="true">
    <defs>
      <linearGradient id="rodShade" x1="0" x2="1">
        <stop offset="0" stop-color="#6d6d6d"/><stop offset=".5" stop-color="#e2e2e2"/><stop offset="1" stop-color="#6d6d6d"/>
      </linearGradient>
      <linearGradient id="panelShade" x1="0" y1="0" x2="0" y2="1">
        <stop offset="0" stop-color="#3a3a3a"/><stop offset=".2" stop-color="#0d0d0d"/><stop offset=".9" stop-color="#0d0d0d"/><stop offset="1" stop-color="#262626"/>
      </linearGradient>
    </defs>
    <!-- hanging rods -->
    <rect x="597" y="0" width="6" height="26" fill="url(#rodShade)"/>
    <rect x="500" y="120" width="9" height="38" fill="url(#rodShade)"/>
    <rect x="685" y="120" width="9" height="38" fill="url(#rodShade)"/>
    <rect x="475" y="426" width="9" height="20" fill="url(#rodShade)"/>
    <rect x="716" y="426" width="9" height="20" fill="url(#rodShade)"/>
    <rect x="475" y="574" width="9" height="14" fill="url(#rodShade)"/>
    <rect x="716" y="574" width="9" height="14" fill="url(#rodShade)"/>
    <rect x="475" y="624" width="9" height="10" fill="url(#rodShade)"/>
    <rect x="716" y="624" width="9" height="10" fill="url(#rodShade)"/>
    <!-- brand sign -->
    <path d="M448 24 Q598 34 748 24 L722 125 Q598 118 474 125 Z" fill="url(#panelShade)"/>
    <!-- high hand wings -->
    <path d="M274 444 L420 450 L420 562 L298 558 Q282 510 274 444 Z" fill="url(#panelShade)"/>
    <path d="M926 444 L780 450 L780 562 L902 558 Q918 510 926 444 Z" fill="url(#panelShade)"/>
    <!-- card tray -->
    <path d="M390 442 Q598 434 805 442 L790 570 Q598 580 410 570 Z" fill="url(#panelShade)"/>
  </svg>

  <div class="brand-name">ACE HOUSE</div>
  <div class="panel-bar panel-bar--jackpot">ROYAL FLUSH JACKPOT</div>

  <div class="odometer-band"></div>
  <div class="odometer" aria-label="Jackpot 256,111.95">
    <div class="digit" style="left:134px">2</div>
    <div class="digit" style="left:248px">5</div>
    <div class="digit" style="left:362px">6</div>
    <div class="separator" style="left:473px">,</div>
    <div class="digit" style="left:486px">1</div>
    <div class="digit" style="left:598px">1</div>
    <div class="digit" style="left:710px">1</div>
    <div class="separator" style="left:821px">,</div>
    <div class="digit" style="left:834px">9</div>
    <div class="digit" style="left:948px">5</div>
  </div>

  <div class="panel-bar panel-bar--bonus">HIGH HAND BONUS</div>

  <div class="prize"><div class="stat-label">PRIZE</div><div class="stat-value">$250</div></div>
  <div class="countdown"><div class="stat-label">COUNTDOWN</div><div class="stat-value">1:59</div></div>

  <div class="hand">
    <div class="card card--red" style="left:442px"><span class="card-corner card-corner--top">A<br>♥</span><span class="card-pip">♥</span><span class="card-corner card-corner--bottom">A<br>♥</span></div>
    <div class="card card--black" style="left:523px"><span class="card-corner card-corner--top">A<br>♣</span><span class="card-pip">♣</span><span class="card-corner card-corner--bottom">A<br>♣</span></div>
    <div class="card card--red" style="left:605px"><span class="card-corner card-corner--top">A<br>♦</span><span class="card-pip">♦</span><span class="card-corner card-corner--bottom">A<br>♦</span></div>
    <div class="card card--black" style="left:686px"><span class="card-corner card-corner--top">A<br>♠</span><span class="card-pip">♠</span><span class="card-corner card-corner--bottom">A<br>♠</span></div>
  </div>

  <div class="panel-bar panel-bar--winner">Two Pair - Table 18 (Sam Carter)</div>
  <div class="news-band">TEXT NEWS HERE</div>
</main>
</body>
</html>
```